Veterinary Clinic Letterhead - Ridgeview Veterinary Surgery

We need a letterhead design for an established Veterinary Clinic in Mareeba called Ridgeview Veterinary Surgery. We are a moderate sized mixed animal veterinary clinic offering a wide variety of veterinary services. The design should use the same colour pattern as those in the logos supplied. The design should also include our address (48 Tulloch Road, Kelso Vale, Queensland, 4871), phone number (07 4158 6734), email (admin@ridgeviewvets.com.au), website (www.ridgeviewvets.com.au) and our opening hours (7:30am to 6pm Monday to Friday and 9am to 1pm Saturday).
Target Market(s)
Pet owners
Industry/Entity Type
Veterinary
Requirements
Must have
- The logo or modification of it, business address, opening hours, website, phone number and email address

```html
<!DOCTYPE html>
<html lang="en">
<head>
<meta charset="utf-8">
<title>Ridgeview Veterinary Surgery – Letterhead</title>
<link rel="stylesheet" href="https://fonts.googleapis.com/css2?family=Lato:ital,wght@0,400;0,700;1,400&family=Open+Sans:ital,wght@0,600;0,700;1,400;1,700&display=swap">
<style>
  :root {
    --backdrop: #8a8a8a;
    --paper: #ffffff;
    --navy: #0e2c55;
    --navy-light: #1a4274;
    --ink: #222222;
    --ink-soft: #444444;
    --watermark: #f1f2f4;
  }
  * { box-sizing: border-box; margin: 0; padding: 0; }
  html, body {
    width: 900px; height: 1200px; overflow: hidden;
    background: var(--backdrop);
  }
  .letterhead {
    position: absolute; left: 150px; top: 176px;
    width: 600px; height: 848px;
    background: var(--paper);
    box-shadow: 0 4px 18px rgba(0,0,0,.25);
    overflow: hidden;
    font-family: "Lato", sans-serif;
    color: var(--ink);
  }
  .header-band {
    position: absolute; left: 0; top: 42px; width: 600px; height: 123px;
    background: linear-gradient(100deg, var(--navy-light) 0%, var(--navy) 45%, var(--navy) 100%);
  }
  .brand {
    position: absolute; left: 38px; top: 0; width: 170px; height: 123px;
    text-align: center; color: #fff;
    font-family: "Open Sans", sans-serif; font-weight: 600;
  }
  .brand-dot {
    width: 58px; height: 58px; border-radius: 50%;
    background: #fff; margin: 10px auto 8px;
  }
  .brand-name { font-size: 11.5px; letter-spacing: .4px; line-height: 1.25; }
  .contact-list {
    position: absolute; left: 330px; top: 10px; list-style: none;
    color: #fff; font-size: 14.5px; line-height: 1.2;
  }
  .contact-list li { display: flex; align-items: flex-start; margin-bottom: 5px; }
  .contact-list svg { width: 13px; height: 13px; margin: 2px 9px 0 0; flex: none; fill: #fff; }
  .watermark {
    position: absolute; left: 175px; top: 205px; width: 300px; height: 300px;
    border-radius: 50%; background: var(--watermark);
  }
  .recipient {
    position: absolute; left: 77px; top: 286px;
    font-family: "Open Sans", sans-serif;
  }
  .recipient-name { font-size: 17px; font-weight: 700; line-height: 1.2; }
  .recipient-address {
    margin-top: 10px; font-style: italic; font-size: 10.5px; line-height: 1.25; color: var(--ink-soft);
  }
  .salutation {
    position: absolute; left: 77px; top: 384px;
    font-family: "Open Sans", sans-serif; font-style: italic; font-weight: 700; font-size: 21px;
    line-height: 1.3;
  }
  .letter-body {
    position: absolute; left: 77px; top: 422px; width: 450px;
    font-size: 8.6px; line-height: 1.38; color: var(--ink);
  }
  .letter-body p { margin-bottom: 11px; }
  .sign-off {
    position: absolute; right: 88px; top: 652px; text-align: right;
    font-size: 8.6px; line-height: 1.45;
  }
  .sign-off strong { font-weight: 700; }
  .signature {
    position: absolute; right: 82px; top: 688px; width: 110px; height: 32px;
    background: linear-gradient(90deg, #e9e9e9, #d6d6d6); border-radius: 3px;
  }
  .footer-band {
    position: absolute; left: 0; top: 785px; width: 600px; height: 42px;
    background: var(--navy); color: #fff;
    display: flex; align-items: center; justify-content: center;
    font-size: 16px; letter-spacing: .2px;
  }
</style>
</head>
<body>
  <div class="letterhead">
    <header class="header-band">
      <div class="brand">
        <div class="brand-dot"></div>
        <div class="brand-name">RIDGEVIEW VETERINARY<br>SURGERY</div>
      </div>
      <ul class="contact-list">
        <li><svg viewBox="0 0 24 24"><path d="M6.6 10.8a15.1 15.1 0 0 0 6.6 6.6l2.2-2.2a1 1 0 0 1 1-.25 11.4 11.4 0 0 0 3.6.57 1 1 0 0 1 1 1V20a1 1 0 0 1-1 1A17 17 0 0 1 3 4a1 1 0 0 1 1-1h3.5a1 1 0 0 1 1 1c0 1.250.2 2.45.57 3.6a1 1 0 0 1-.25 1z"/></svg>07 4158 6734</li>
        <li><svg viewBox="0 0 24 24"><path d="M12 2a7 7 0 0 0-7 7c0 5.25 7 13 7 13s7-7.75 7-13a7 7 0 0 0-7-7zm0 9.5A2.5 2.5 0 1 1 12 6.5a2.5 2.5 0 0 1 0 5z"/></svg>48 Tulloch Road, Kelso Vale,<br>Queensland, 4871</li>
        <li><svg viewBox="0 0 24 24"><path d="M2 5h20v14H2z M2 5l10 8 10-8" stroke="#0e2c55" stroke-width="1.6"/></svg>admin@ridgeviewvets.com.au</li>
        <li><svg viewBox="0 0 24 24"><circle cx="12" cy="12" r="10"/><path d="M2 12h20M12 2c3 3 3 17 0 20M12 2c-3 3-3 17 0 20" stroke="#0e2c55" stroke-width="1.4" fill="none"/></svg>www.ridgeviewvets.com.au</li>
      </ul>
    </header>

    <div class="watermark" aria-hidden="true"></div>

    <section class="recipient">
      <div class="recipient-name">To: Mark Ellison<br>CEO of Harbourline Group</div>
      <div class="recipient-address">West Street 123<br>Los Angeles, CA<br>USA</div>
    </section>

    <div class="salutation">Dear Sir,</div>

    <main class="letter-body">
      <p>Thank you for choosing our clinic for the care of your animals. Our team has looked after pets, working dogs and livestock across the Tablelands for many years, and we remain committed to practical, honest and compassionate care. This letter sets out the details of the services we discussed and the next steps we recommend for your herd and household pets this season.</p>
      <p>Our veterinarians can visit your property for routine vaccinations, pregnancy testing and herd health checks, while small animal consultations, surgery, dental care and diagnostic imaging are available at the clinic. We will prepare a written estimate before any procedure and discuss every option with you in plain terms. Appointments can be arranged by phone or email, and urgent cases are always given priority during our opening hours.</p>
      <p>Please review the enclosed schedule and let us know if any dates need to change. We look forward to working with you and your animals again soon.</p>
    </main>

    <div class="sign-off">Yours sincerely,<br><strong>Daniel Peter Whitford</strong></div>
    <div class="signature" role="img" aria-label="Handwritten signature"></div>

    <footer class="footer-band">7:30am to 6pm Monday to Friday and 9am to 1pm Saturday</footer>
  </div>
</body>
</html>
```